Brochure Design Project for Family and Cosmetic Dental Practice

Family and Cosmetic Dental Practice with Ocean/Tropical Theme
Here is some more information about my business. We also have a website :www.marlowcrestsmiles.com. That has a video that we made and gives you a some more information about us.

An Overview / Background of the Business & Services :

Family and Cosmetic Dental Practice

Procedures that we do:

Clearmora (Clear Braces)

Dentures and Partials

Whitening/ Teeth Bleaching (both Brite and Vel)

Cosmetic Dentistry (veneers and esthetic crowns)

Implants

Children's Dentistry

Sedation Dentistry and Nitrous Oxide Gas (Laughing Gas)

The Target Market / Audience you are trying to reach:

Families (30 to 40 yrs with children) - Caucasians and Hispanics
People seeking cosmetic dentistry
Older Patients (50yrs +)

Design Specifics; any preferences or ideas for Style, Colour, Imagery, etc :

Color: Blues

Theme: Ocean/ Tropical

Our Philosophy

Our belief is that the best oral care that you receive is at home where you are able to maintain your oral hygiene through proper brushing, flossing and control of your diet. We would like to see you maintain your natural teeth for the rest of your life. When this is not possible we will work with you to replace them with the best aesthetic and functional restorative dentistry
that is available.

We want to let people we have been at our location for 10 years and we are family owned and are here for the long run. We are active in the community

Bios of the doctors: ( I already sent the headshot photos)

Dr Leonard Whitcombe
“Dr. Lenny”

Dr. Lenny Whitcombe attended Pemberton University for his undergraduate studies and earned a Bachelor’s degree in Chemistry. While attending Pemberton he pursued his passion of running and was a member of two Prairie Athletic League Champion cross country teams. His passion for running evolved into a desire to compete in triathlons. He continued his interest in the sciences and working with his hands by attending the Ashgrove State University College of Dentistry where he met his wife, Clara Whitcombe D.D.S. and earned his D.D.S. with honors in Oral Surgery. He has practiced the last few years in Tucson treating a wide range of patients. His desire to practice dentistry revolves around the patient and service. Some of his hobby highlights include finishing the Desert Ridge Endurance triathlon in 11 hours and 37 minutes in 2005 and a single digit golf handicap. His current passion is mountain biking. He recently finished the Ridgecrest Trail Cycling race (100 miles in one day)! Lately he spends a lot of time caring for and playing with his 3 daughters. Dr. Lenny Whitcombe is also a member of NOA (National Oral Alliance), StOC (State Oral Care Society) and GPF (Guild of Practice Fellows).

Dr. Clara Whitcombe
“Dr. Whitcombe”

Dr. Clara Whitcombe attended both Halvern College and Eastbrook Wesleyan College for her undergraduate degrees. She received a Bachelor of Science in Biology and a Bachelor of Arts in Psychology. After college, Dr Whitcombe worked for several years in the dental field while continuing her education by working towards a Master’s degree in Cell and Molecular Biology. At this point in her life Dr. Whitcombe knew that she enjoyed the dental field and decided to attend dental school. Dr. Whitcombe completed her Doctorate of Dental Surgery (D.D.S.) at Ashgrove State University where she met her husband, Dr. Leonard Whitcombe. They then moved to Tucson, Arizona in order to be close to family. When Dr. Clara isn't in the office creating beautiful smiles, she is busy with her 3 daughters and their numerous activities. Dr. Clara Whitcombe has additional training in the areas of endodontics and oral sedation. She is also a member of The National Guild of Practice Fellows (NGPF), National Oral Alliance (NOA), and State Oral Care Society (StOC). In her time outside of the office, Dr. Whitcombe enjoys traveling, spending time with her family, working out and being involved with book club.
Let me know if you need anything else!

Target Market(s)

See above

Industry/Entity Type

Business

Colors
33a6d7
85cae6
33b8a4

Requirements
Must have
• Testimonials taken from Rateway reviews. In any images used, the people must have nice smiles and teeth.

```html
<!DOCTYPE html>
<html lang="en">
<head>
<meta charset="utf-8">
<title>Smile with confidence – Marlowcrest Family Dentistry</title>
<link href="https://fonts.googleapis.com/css2?family=Open+Sans:wght@400;600;700&display=swap" rel="stylesheet">
<style>
  :root {
    --navy: #1d4f7c;
    --ocean: #33a6d7;
    --sky: #85cae6;
    --teal: #33b8a4;
    --ink: #3a3f45;
    --paper: #ffffff;
    --mist: #eef7fb;
  }
  * { margin: 0; padding: 0; box-sizing: border-box; }
  html, body { width: 755px; height: 1200px; overflow: hidden; background: var(--paper); }
  body { font-family: "Open Sans", Arial, sans-serif; color: var(--ink); }
  .brochure { position: relative; width: 755px; height: 1200px; background: var(--paper); overflow: hidden; }

  .hero-scene {
    position: absolute; left: 0; top: 0; width: 755px; height: 260px;
    background: linear-gradient(180deg, #4fa8d8 0%, #8fcbe8 38%, #d8eef7 70%, rgba(255,255,255,0) 100%);
  }
  .palm-shade {
    position: absolute; left: 0; top: 0; width: 330px; height: 150px;
    background: radial-gradient(ellipse at 20% 20%, rgba(34,90,60,.55) 0%, rgba(34,90,60,0) 70%);
  }
  .headline {
    position: absolute; right: 38px; top: 26px; text-align: left;
    color: var(--navy); line-height: 1;
  }
  .headline .lead { display: block; font-size: 34px; font-weight: 400; }
  .headline .strong { display: block; font-size: 40px; font-weight: 700; margin-left: 2px; }

  .doctor { position: absolute; left: 30px; width: 700px; }
  .doctor-one { top: 170px; }
  .doctor-two { top: 615px; }

  .portrait {
    position: absolute; left: 0; width: 142px; background: var(--paper);
    box-shadow: 0 1px 4px rgba(0,0,0,.25);
  }
  .doctor-one .portrait { top: 58px; }
  .doctor-two .portrait { top: 0; }
  .portrait-photo { display: block; width: 142px; height: 185px; }
  .portrait-caption {
    background: var(--ocean); color: #fff; padding: 6px 8px 7px;
    font-size: 11px; line-height: 1.3;
  }
  .portrait-caption strong { display: block; font-weight: 700; }

  .bio {
    position: absolute; left: 162px; top: 0; width: 538px;
    font-size: 13.2px; line-height: 21.6px; text-align: justify;
  }
  .bio p + p { margin-top: 2px; }

  .footer {
    position: absolute; left: 0; bottom: 0; width: 755px; height: 112px;
    border-top: 3px solid var(--sky);
    display: flex; align-items: center; padding: 0 30px;
    background: linear-gradient(180deg, var(--mist), #fff);
  }
  .brand { display: flex; align-items: center; gap: 10px; width: 250px; }
  .brand-dot { width: 34px; height: 34px; border-radius: 50%; background: var(--ocean); flex: none; }
  .brand-name { font-size: 16px; font-weight: 700; color: var(--navy); line-height: 1.15; }
  .address, .contact { font-size: 13.5px; line-height: 20px; color: var(--ink); }
  .address { width: 260px; padding-left: 14px; border-left: 1px solid var(--sky); }
  .contact { margin-left: auto; padding-left: 14px; border-left: 1px solid var(--sky); }
</style>
</head>
<body>
<main class="brochure">
  <div class="hero-scene" role="img" aria-label="Tropical beach scene with palm fronds and blue sky"><div class="palm-shade"></div></div>

  <h1 class="headline"><span class="lead">Smile with</span><span class="strong">confidence</span></h1>

  <section class="doctor doctor-one">
    <figure class="portrait">
      <svg class="portrait-photo" viewBox="0 0 142 185" role="img" aria-label="Portrait photo of Dr. Leonard Whitcombe">
        <defs><linearGradient id="p1" x1="0" y1="0" x2="0" y2="1"><stop offset="0" stop-color="#c9d2d8"/><stop offset="1" stop-color="#8e9aa5"/></linearGradient></defs>
        <rect width="142" height="185" fill="url(#p1)"/>
      </svg>
      <figcaption class="portrait-caption"><strong>Dr Leonard Whitcombe</strong>Dr. Lenny</figcaption>
    </figure>
    <div class="bio">
      <p>Dr. Lenny Whitcombe attended Pemberton University for his undergraduate studies and earned a Bachelor’s degree in Chemistry. While attending Pemberton he pursued his passion of running and was a member of two Prairie Athletic League Champion cross country teams. His passion for running evolved into a desire to compete in triathlons. He continued his interest in the sciences and working with his hands by attending the Ashgrove State University College of Dentistry where he met his wife, Clara Whitcombe D.D.S. and earned his D.D.S. with honors in Oral Surgery. He has practiced the last few years in Tucson treating a wide range of patients. His desire to practice dentistry revolves around the patient and service. Some of his hobby highlights include finishing the Desert Ridge Endurance triathlon in 11 hours and 37 minutes in 2005 and a single digit golf handicap. His current passion is mountain biking. He recently finished the Ridgecrest Trail Cycling race (100 miles in one day)! Lately he spends a lot of time caring for and playing with his 3 daughters. Dr. Lenny Whitcombe is also a member of NOA (National Oral Alliance), StOC (State Oral Care Society) and GPF (Guild of Practice Fellows).</p>
    </div>
  </section>

  <section class="doctor doctor-two">
    <figure class="portrait">
      <svg class="portrait-photo" viewBox="0 0 142 185" role="img" aria-label="Portrait photo of Dr. Clara Whitcombe">
        <defs><linearGradient id="p2" x1="0" y1="0" x2="0" y2="1"><stop offset="0" stop-color="#d9d4cc"/><stop offset="1" stop-color="#9e8f7e"/></linearGradient></defs>
        <rect width="142" height="185" fill="url(#p2)"/>
      </svg>
      <figcaption class="portrait-caption"><strong>Dr. Clara Whitcombe</strong>Dr. Whitcombe</figcaption>
    </figure>
    <div class="bio">
      <p>Dr. Clara Whitcombe attended both Halvern College and Eastbrook Wesleyan College for her undergraduate degrees. She received a Bachelor of Science in Biology and a Bachelor of Arts in Psychology. After college, Dr Whitcombe worked for several years in the dental field while continuing her education by working towards a Master’s degree in Cell and Molecular Biology. At this point in her life Dr. Whitcombe knew that she enjoyed the dental field and decided to attend dental school. Dr. Whitcombe completed her Doctorate of Dental Surgery (D.D.S.) at Ashgrove State University where she met her husband, Dr. Leonard Whitcombe. They then moved to Tucson, Arizona in order to be close to family. When Dr. Clara isn’t in the office creating beautiful smiles, she is busy with her 3 daughters and their numerous activities. Dr. Clara Whitcombe has additional training in the areas of endodontics and oral sedation. She is also a member of The National Guild of Practice Fellows (NGPF), National Oral Alliance (NOA), and State Oral Care Society (StOC). In her time outside of the office, Dr. Whitcombe enjoys traveling, spending time with her family, working out and being involved with book club.</p>
      <p>Let me know if you need anything else!</p>
    </div>
  </section>

  <footer class="footer">
    <div class="brand"><span class="brand-dot"></span><span class="brand-name">Marlowcrest<br>Family Dentistry</span></div>
    <address class="address" style="font-style:normal">1480 West Harbor Vista Road<br>Suite 204<br>Coralton, AZ 85011</address>
    <div class="contact">Phone: 480-555-0142<br>Fax: 480-555-0187<br>mcsmiles@mailbox.com</div>
  </footer>
</main>
</body>
</html>
```